Kelvane Plumbing Business cards

Company is Kelvane Plumbing.
name Dashel Morrowby, I am a plumber, drainer, gasfitter and roofer
Mobile: 0431 906 154
Email address: info@kelvaneplumbing.example (check out my website for some ideas)
Website: www.kelvaneplumbing.example
ABN: 82 916 203 471
LIC: 604517K

I am reliable all round plumber. I am a 24 hour emergency service. Kelvane Plumbing is a professional plumbing service in the Illawarra, South Coast, Southern Sydney and Southern Highland regions of NSW. We offer a 24 hour emergency service for piece of mind to our customers. Call us now to see how we can help you. Kelvane Plumbing approaches every job with attention to detail and excellent customer service. With our superior workmanship you can be confident that the job will be done right the first time around. You can rest assured with results that are guaranteed to last.

Target Market(s)

the general public

Contact Information for Business Card

look up website for some ideas something with similar colours to logo and new modern and to catch the eye.

Colors
fdfdfd
ffffff
000000
7f7f7f
aaaaaa
33a6d7
0492cd

Requirements
Must have
• all contact details
• company- Kelvane Plumbing
• name- Dashel Morrowby
• number mobile- 0431 906 154
• Email address- info@kelvaneplumbing.example
• Website- www.kelvaneplumbing.example
• ABN- 82 916 203 471
• LIC- 604517K

```html
<!DOCTYPE html>
<html lang="en">
<head>
<meta charset="utf-8">
<title>Kelvane Plumbing – Business Cards</title>
<link rel="stylesheet" href="https://fonts.googleapis.com/css2?family=Open+Sans:ital,wght@0,400;0,700;1,400&display=swap">
<style>
  :root {
    --stage: #d6d7d9;
    --paper: #e6e6e6;
    --ink: #000000;
    --panel-dark: #000000;
    --logo-tile: #141414;
    --brand-blue: #33a6d7;
    --brand-grey: #7f7f7f;
    --text: #111111;
    --white: #ffffff;
  }
  * { box-sizing: border-box; margin: 0; padding: 0; }
  html, body { width: 1200px; height: 1200px; overflow: hidden; }
  body {
    background: var(--stage);
    font-family: "Open Sans", Arial, sans-serif;
    color: var(--text);
    position: relative;
  }
  .card {
    position: absolute;
    left: 150px;
    width: 900px;
    height: 550px;
    border: 4px solid var(--ink);
    background: var(--paper);
    overflow: hidden;
  }
  .card--front { top: 30px; }
  .card--back { top: 620px; }

  .panel { position: absolute; top: 0; bottom: 0; }
  .panel--light { background: var(--paper); }
  .panel--dark { background: var(--panel-dark); }

  .card--front .panel--light { left: 0; width: 330px; }
  .card--front .panel--dark { left: 330px; right: 0; }
  .card--back .panel--dark { left: 0; width: 330px; }
  .card--back .panel--light { left: 330px; right: 0; }

  .website {
    position: absolute;
    writing-mode: vertical-rl;
    transform: rotate(180deg);
    font-size: 30px;
    letter-spacing: 0.5px;
    white-space: nowrap;
    color: var(--text);
  }
  .card--front .website { left: 140px; top: 50%; translate: 0 -50%; }
  .card--back .website { right: 22px; top: 50%; translate: 0 -50%; font-size: 28px; }

  .brand-tile {
    position: absolute;
    background: var(--logo-tile);
    display: flex;
    align-items: center;
    justify-content: center;
  }
  .brand-ring {
    border: 10px solid var(--brand-grey);
    border-radius: 50%;
    display: flex;
    align-items: center;
    justify-content: center;
    text-align: center;
  }
  .brand-name {
    color: var(--brand-blue);
    font-weight: 700;
    text-transform: uppercase;
    line-height: 1.1;
  }
  .card--front .brand-tile { left: 432px; top: 88px; width: 366px; height: 366px; }
  .card--front .brand-ring { width: 320px; height: 320px; }
  .card--front .brand-name { font-size: 40px; letter-spacing: 1px; }

  .card--back .brand-tile { left: 82px; top: 190px; width: 166px; height: 166px; }
  .card--back .brand-ring { width: 146px; height: 146px; border-width: 6px; }
  .card--back .brand-name { font-size: 17px; }

  .holder-name {
    position: absolute;
    left: 355px; top: 40px;
    font-size: 33px;
    font-weight: 700;
  }
  .holder-role {
    position: absolute;
    left: 355px; top: 94px;
    font-size: 19px;
  }
  .contact-list { list-style: none; position: absolute; left: 350px; top: 162px; }
  .contact-item {
    display: flex;
    align-items: center;
    gap: 14px;
    height: 86px;
    font-size: 22px;
  }
  .contact-badge {
    width: 50px; height: 50px;
    border-radius: 50%;
    background: var(--ink);
    color: var(--white);
    display: flex; align-items: center; justify-content: center;
    font-size: 16px; font-style: italic;
    flex: none;
  }
  .contact-badge svg { width: 28px; height: 28px; }
</style>
</head>
<body>

<section class="card card--front" aria-label="Card front">
  <div class="panel panel--light">
    <p class="website">www.kelvaneplumbing.example</p>
  </div>
  <div class="panel panel--dark"></div>
  <div class="brand-tile">
    <div class="brand-ring"><p class="brand-name">Kelvane<br>Plumbing</p></div>
  </div>
</section>

<section class="card card--back" aria-label="Card back">
  <div class="panel panel--dark"></div>
  <div class="brand-tile">
    <div class="brand-ring"><p class="brand-name">Kelvane<br>Plumbing</p></div>
  </div>
  <div class="panel panel--light"></div>
  <h1 class="holder-name">Dashel Morrowby</h1>
  <p class="holder-role">Plumber, Drainer, Gasfitter and roofer</p>
  <ul class="contact-list">
    <li class="contact-item">
      <span class="contact-badge">
        <svg viewBox="0 0 24 24" fill="none" stroke="#fff" stroke-width="1.8"><rect x="7" y="2.5" width="10" height="19" rx="2"/><line x1="11" y1="18.5" x2="13" y2="18.5"/></svg>
      </span>
      0431 906 154
    </li>
    <li class="contact-item">
      <span class="contact-badge">
        <svg viewBox="0 0 24 24" fill="none" stroke="#fff" stroke-width="1.8"><rect x="3" y="6" width="18" height="12" rx="1"/><polyline points="3,6 12,13 21,6"/></svg>
      </span>
      info@kelvaneplumbing.example
    </li>
    <li class="contact-item">
      <span class="contact-badge">ABN</span>
      82 916 203 471
    </li>
    <li class="contact-item">
      <span class="contact-badge">LIC</span>
      604517K
    </li>
  </ul>
  <p class="website">www.kelvaneplumbing.example</p>
</section>

</body>
</html>
```